Business Card Design Project

I have just chosen a logo and would now like this designed onto a business card for my hair salon. I would like it to be classy not to busy and have a wow factor when people look at them
Has to Include on card:
Logo Design
And business details below
Kellie-ann Drummond (owner)
0482 736 219
Rdw@vomblet.com.au
71 Willowmere Rise Corvin Cove
Logo is now attached please provide designs
Hair

```html
<!DOCTYPE html>
<html lang="en">
<head>
<meta charset="utf-8">
<title>Lumen Hair Studio — Business Card</title>
<link href="https://fonts.googleapis.com/css2?family=Cabin:wght@400;500;600&display=swap" rel="stylesheet">
<style>
  :root {
    --page-bg: #2b2b2d;
    --card-top: #10131f;
    --card-bottom: #06070d;
    --back-light: #2a2c36;
    --back-dark: #0e0f15;
    --magenta: #d6187a;
    --teal: #5fb8c2;
  }
  * { margin: 0; padding: 0; box-sizing: border-box; }
  html, body {
    width: 1200px;
    height: 900px;
    overflow: hidden;
    background: var(--page-bg);
  }
  .canvas {
    position: relative;
    width: 1200px;
    height: 900px;
    font-family: "Cabin", sans-serif;
  }
  .card {
    position: absolute;
    left: 250px;
    width: 700px;
    height: 400px;
    border-radius: 26px;
    overflow: hidden;
  }
  .card-back { top: 35px; }
  .card-front {
    top: 465px;
    background: linear-gradient(160deg, var(--card-top), var(--card-bottom));
  }
  .back-surface {
    position: absolute;
    inset: 0;
    background: linear-gradient(120deg, var(--back-dark) 0%, var(--back-light) 38%, var(--back-dark) 55%, var(--back-light) 78%, var(--back-dark) 100%);
  }
  .brand-name {
    position: absolute;
    text-align: center;
    color: var(--magenta);
    font-weight: 600;
    line-height: 1.08;
    letter-spacing: 3px;
    text-transform: uppercase;
  }
  .card-back .brand-name {
    left: 0;
    width: 100%;
    top: 125px;
    font-size: 46px;
  }
  .card-front .brand-name {
    left: 140px;
    width: 380px;
    top: 62px;
    font-size: 38px;
  }
  .swooshes {
    position: absolute;
    inset: 0;
  }
  .contact-list {
    position: absolute;
    left: 400px;
    top: 225px;
    list-style: none;
    color: var(--teal);
    font-size: 16px;
    line-height: 1.65;
  }
  .contact-list li {
    display: flex;
    align-items: center;
    gap: 9px;
  }
  .contact-list svg {
    width: 14px;
    height: 14px;
    fill: var(--magenta);
    flex: none;
  }
  .owner {
    position: absolute;
    left: 40px;
    top: 300px;
  }
  .owner-name {
    color: var(--magenta);
    font-size: 22px;
    font-weight: 500;
  }
  .owner-role {
    color: var(--teal);
    font-size: 15px;
    font-weight: 600;
    margin-top: 2px;
  }
</style>
</head>
<body>
<div class="canvas">
  <div class="card card-back">
    <div class="back-surface" role="img" aria-label="Soft diagonal faceted pattern in charcoal tones"></div>
    <div class="brand-name">Lumen<br>Hair Studio</div>
  </div>

  <div class="card card-front">
    <svg class="swooshes" viewBox="0 0 700 400" aria-hidden="true">
      <path d="M330,232 Q520,200 700,100 L700,118 Q520,214 330,232 Z" fill="var(--magenta)"/>
      <path d="M0,262 Q360,222 700,124 L700,134 Q360,236 0,274 Z" fill="var(--teal)"/>
    </svg>

    <div class="brand-name">Lumen<br>Hair Studio</div>

    <ul class="contact-list">
      <li>
        <svg viewBox="0 0 24 24"><path d="M6.6 10.8a15 15 0 0 0 6.6 6.6l2.2-2.2a1 1 0 0 1 1-.25 11.4 11.4 0 0 0 3.6.57 1 1 0 0 1 1 1V20a1 1 0 0 1-1 1A17 17 0 0 1 3 4a1 1 0 0 1 1-1h3.5a1 1 0 0 1 1 1c0 1.25.2 2.45.57 3.6a1 1 0 0 1-.25 1z"/></svg>
        0482 736 219
      </li>
      <li>
        <svg viewBox="0 0 24 24"><path d="M2 5h20v14H2z M3 6l9 7 9-7" fill="none" stroke="var(--magenta)" stroke-width="2"/></svg>
        Rdw@vomblet.com.au
      </li>
      <li>
        <svg viewBox="0 0 24 24"><path d="M12 2a7 7 0 0 0-7 7c0 5 7 13 7 13s7-8 7-13a7 7 0 0 0-7-7zm0 9.5A2.5 2.5 0 1 1 12 6.5a2.5 2.5 0 0 1 0 5z"/></svg>
        71 Willowmere Rise Corvin Cove
      </li>
    </ul>

    <div class="owner">
      <div class="owner-name">Kellie-ann Drummond</div>
      <div class="owner-role">owner</div>
    </div>
  </div>
</div>
</body>
</html>
```